Harbourline Interiors Group Corporate Brochure

we are looking for submissions to design our company corporate brochure for print and PDF.
please find attached the booklet info with photos and words. please note the power point is the case study. the case study photos must be used for the case study (not all of them) with those words that are in there.
please feel free to use lifestyle pictures such as medical commercial hospitalities offices fit outs like the ones attached. for background photos
please make sure the brochure is make in pages of 4 for print (4 pages, or 8 pages or 12 pages or 16 pages ect)
any further questions please ask us

```html
<!DOCTYPE html>
<html lang="en">
<head>
<meta charset="utf-8">
<title>Harbourline Interiors Group – Corporate Brochure</title>
<link rel="stylesheet" href="https://fonts.googleapis.com/css2?family=Archivo+Black&family=Montserrat:wght@400;600;700&display=swap">
<style>
:root{
  --blue:#2d7cc8;
  --blue-deep:#1c58b3;
  --blue-light:#5bb8ea;
  --ink:#1d1d1d;
  --ink-soft:#444a52;
  --paper:#ffffff;
  --stage:#8f9297;
  --photo-light:#e7eaee;
  --photo-mid:#b9bfc6;
  --photo-warm:#a98a6a;
}
*{margin:0;padding:0;box-sizing:border-box}
html,body{width:676px;height:1200px;overflow:hidden;background:var(--stage)}
body{font-family:"Montserrat",sans-serif;color:var(--ink)}
.spread{position:absolute;left:17px;top:264px;display:grid;grid-template-columns:repeat(4,155px);grid-auto-rows:219px;gap:7px}
.page{position:relative;overflow:hidden;background:var(--paper)}
.abs{position:absolute}
.photo{position:absolute;background:linear-gradient(160deg,var(--photo-light),var(--photo-mid))}
.photo--warm{background:linear-gradient(150deg,#efe9e1,var(--photo-warm) 60%,#3b5f7c)}
.photo--site{background:linear-gradient(170deg,#d9d6d0,#8d8983)}
.photo--dark{background:linear-gradient(170deg,#6a6d70,#2c2e31)}
.photo--person{background:linear-gradient(180deg,#c9b8a6,#2a3550)}
.photo--keys{background:linear-gradient(135deg,#dfe3e8,#9aa3ad 60%,#d23b3b)}
.photo--fade{background:linear-gradient(180deg,rgba(255,255,255,0),#c9d3e3)}
.head{font-family:"Archivo Black",sans-serif;text-transform:uppercase;line-height:1.05}
.body{font-size:2.35px;line-height:1.42;color:var(--ink-soft)}
.body p{margin-bottom:1.8px}
.brand{font-family:"Archivo Black",sans-serif;color:#fff;font-size:6.2px;line-height:1.05;text-transform:uppercase;display:flex;align-items:center;gap:4px}
.brand__mark{width:9px;height:9px;background:#fff;flex:none}
.pnum{position:absolute;bottom:4px;font-size:2.8px;font-weight:700;color:var(--blue-deep);border-bottom:1px solid var(--blue-deep);padding:0 1px}
.pnum--l{left:7px}.pnum--r{right:7px}
.blue-txt{color:var(--blue-deep)}
.bullets li{list-style:none;position:relative;padding-left:4px}
.bullets li::before{content:"";position:absolute;left:0;top:1px;width:1.4px;height:1.4px;background:var(--blue-deep)}

/* back cover */
.back{background:var(--blue)}
.back__lower{left:0;right:0;top:110px;bottom:0;background:var(--ink)}
.back .brand{left:32px;top:24px}
.concl__frame{left:17px;top:108px;width:121px;height:38px;background:var(--blue)}
.concl{left:24px;top:80px;width:107px;height:63px;background:var(--ink);color:#fff;padding:4px 4px}
.concl h3{font-size:5px;font-weight:700;margin-bottom:1.5px}
.concl .body{color:#e5e5e5;font-size:2.2px}
.enquire{left:0;right:0;top:152px;text-align:center;color:#fff}
.enquire h4{font-size:3.2px;font-weight:700;margin-bottom:3px}
.enquire p{font-size:2.2px;line-height:1.3}
.contacts{left:52px;top:178px;color:#fff;font-size:2.2px}
.contacts li{list-style:none;display:flex;align-items:flex-start;gap:3px;margin-bottom:2.4px}
.contacts svg{width:4px;height:4px;flex:none}

/* front cover */
.front{background:var(--blue)}
.front__top{left:0;right:0;top:0;height:98px;background:var(--ink)}
.front__fade{left:0;right:0;top:150px;bottom:0;background:linear-gradient(180deg,var(--blue),#3f8fd4)}
.front .brand{left:18px;top:24px;font-size:7px}
.front__frame{left:17px;top:74px;width:128px;height:70px;background:var(--ink)}
.front__border{left:17px;top:74px;width:122px;height:66px;background:var(--blue)}
.front__url{right:0;bottom:6px;width:80px;height:6px;background:var(--blue-light);font-size:2.7px;color:var(--blue-deep);text-align:right;padding:1.4px 5px 0 0}

/* welcome */
.welcome__title{left:6px;top:6px;font-size:5.6px}
.welcome__body{left:6px;top:20px;width:143px}
.band{left:0;right:0;top:107px;bottom:0;background:var(--blue-deep)}
.band .pnum{color:#fff;border-color:#fff}

/* story */
.story__band{left:0;right:0;top:0;height:113px;background:var(--blue-deep)}
.story__title{left:6px;top:119px;font-size:5.6px;color:var(--blue-deep)}
.story__body{left:6px;top:127px;width:143px}

/* people */
.person__box{left:78px;top:0;width:77px;height:74px;background:var(--blue-deep);display:flex;align-items:center;padding-left:6px}
.person__box--dark{background:var(--ink);left:77px;width:73px;top:6px;height:68px}
.person__edge{left:70px;top:0;width:85px;height:6px;background:var(--blue-deep)}
.person__name{color:#fff;font-size:7px}
.person__body{left:6px;top:80px;width:143px}

/* teams */
.teams__band{left:0;right:0;top:0;height:118px;background:var(--blue-deep)}
.teams__title{left:6px;top:121px;font-size:5.4px;color:var(--blue-deep)}
.team{left:6px;width:143px}
.team__head{display:flex;gap:3px;align-items:flex-end;font-size:3px;font-weight:600;line-height:1.05}
.icon-box{width:8px;height:8px;border:0.6px solid var(--blue-deep);flex:none;display:flex;align-items:center;justify-content:center}
.icon-box i{display:block;width:4px;height:4px;background:var(--blue-light)}

/* services */
.services__title{left:6px;top:5px;font-size:5.4px;color:var(--blue-deep)}
.services__sub{left:6px;top:12px;font-size:2.3px;color:var(--ink-soft)}
.svc{width:70px;display:flex;gap:2.5px;font-size:2.2px;line-height:1.25;color:var(--ink-soft)}
.svc b{color:var(--blue-deep);display:block;font-weight:700}
.svc .icon-box{width:7px;height:7px}
.services__band{left:0;right:0;top:112px;bottom:0;background:var(--blue-deep)}

/* process */
.process__intro{left:10px;top:5px;width:135px;text-align:center;font-size:2.4px;line-height:1.35;color:var(--ink-soft)}
.step{position:absolute;left:0;width:155px;height:26px}
.step svg{position:absolute;top:0;width:22px;height:25px}
.step__title{position:absolute;top:7px;font-size:3.3px;font-weight:600;color:var(--blue-deep);line-height:1.15}
.step__desc{position:absolute;top:3px;width:54px;font-size:1.7px;line-height:1.3;color:var(--ink-soft)}

/* case study */
.case__label{left:6px;top:110px;font-size:2.9px;font-weight:600}
.case__title{left:6px;top:118px;width:70px;font-size:4.5px;font-weight:700;color:var(--blue-deep);line-height:1.15}
.case__meta{left:6px;top:139px;width:70px;font-size:2.6px;line-height:1.5}
.case__meta b{font-weight:600}
.case__list{left:6px;top:160px;width:70px;font-size:2.1px;line-height:1.3;color:var(--ink-soft)}
.case__list li{margin-bottom:3px}

/* build pages */
.build{background:var(--blue-deep)}
.caption{border:0.8px solid #fff;color:#fff;font-size:2.6px;font-weight:600;line-height:1.35;padding:3px}
.caption span{display:block;background:var(--blue-deep)}
</style>
</head>
<body>
<main class="spread">

  <!-- back cover -->
  <section class="page back">
    <div class="abs back__lower"></div>
    <div class="abs brand"><span class="brand__mark"></span><span>Harbourline<br>Interiors<br>Group</span></div>
    <div class="abs concl__frame"></div>
    <div class="abs concl">
      <h3>Conclusion</h3>
      <div class="body">
        <p>By following this structured process methodology, HIG can navigate the complexities of designing and constructing compliant commercial interiors in alignment with the stringent requirements of the Victorian Building Authority. This approach not only ensures legal compliance but also enhances project efficiency, safety, and client satisfaction.</p>
        <p>If you are in search of a fresh approach to guarantee superior outcomes for your upcoming commercial interior fitouts please contact us.</p>
      </div>
    </div>
    <div class="abs enquire">
      <h4>For all enquires contact:</h4>
      <p>Daniel Ashworth – CEO | Founder | Harbourline Interiors Group Pty Ltd<br>Registered Commercial Builder # CB-L 20417<br>Registered Building Design (Interior) # DP-ID 31</p>
    </div>
    <ul class="abs contacts">
      <li><svg viewBox="0 0 10 10"><circle cx="5" cy="5" r="5" fill="#fff"/><path d="M3.3 2.6l1 1-.6.8c.4.9 1 1.5 1.9 1.9l.8-.6 1 1-.8.9C4.7 7.4 2.6 5.3 2.4 3.4z" fill="#1d1d1d"/></svg><span>0400 118 326</span></li>
      <li><svg viewBox="0 0 10 10"><circle cx="5" cy="5" r="5" fill="#fff"/><rect x="2.5" y="3.2" width="5" height="3.6" fill="none" stroke="#1d1d1d" stroke-width=".7"/><path d="M2.5 3.2L5 5.2 7.5 3.2" fill="none" stroke="#1d1d1d" stroke-width=".7"/></svg><span>daniel@harbourlineinteriors.com</span></li>
      <li><svg viewBox="0 0 10 10"><circle cx="5" cy="5" r="5" fill="#fff"/><circle cx="5" cy="5" r="2.6" fill="none" stroke="#1d1d1d" stroke-width=".6"/><path d="M2.4 5h5.2M5 2.4v5.2" stroke="#1d1d1d" stroke-width=".5"/></svg><span>www.harbourlineinteriors.com</span></li>
      <li><svg viewBox="0 0 10 10"><circle cx="5" cy="5" r="5" fill="#fff"/><path d="M5 8C3.6 6.4 3 5.3 3 4.3a2 2 0 014 0C7 5.3 6.4 6.4 5 8z" fill="#1d1d1d"/></svg><span>Level 4, 88 Quayside Road,<br>Melbourne VIC 3000</span></li>
    </ul>
  </section>

  <!-- front cover -->
  <section class="page front">
    <div class="abs front__top"></div>
    <div class="abs front__fade"></div>
    <div class="abs brand"><span class="brand__mark"></span><span>Harbourline<br>Interiors<br>Group</span></div>
    <div class="abs front__frame"></div>
    <div class="abs front__border"></div>
    <div class="photo" style="left:23px;top:80px;width:110px;height:54px" role="img" aria-label="Bright white pharmacy interior with counters and shelving"></div>
    <div class="abs front__url">www.harbourlineinteriors.com</div>
  </section>

  <!-- welcome -->
  <section class="page">
    <h2 class="abs head welcome__title"><span class="blue-txt">Welcome to</span><br>Harbourline Interiors Group!</h2>
    <div class="abs body welcome__body">
      <p>At Harbourline Interiors Group (HIG), we were founded with your needs at the forefront—a dedication to delivering transformative results for your commercial and retail projects.</p>
      <p>Our pride lies in surpassing client expectations through meticulous planning and proactive problem-solving. HIG specializes in:</p>
      <ul class="bullets" style="margin-bottom:1.8px">
        <li>Pharmacy, medical centers, allied health, retail, hospitality, and commercial interior fitouts.</li>
        <li>General tenancy relocations, renovations, rebranding, demolishing, and make good of existing sites.</li>
        <li>Pre-lease based building site inspections and reports.</li>
        <li>Costings, feasibility studies on the design and construction of projects.</li>
      </ul>
      <p>Our competitive edge lies in our proficiency in delivering professional services, ensuring compliance, and providing informed recommendations. We prioritize the protection of our clients across all facets of the interior design business, including on-site safety in accordance with WorkSafe standards. Additionally, we have a nuanced understanding of the construction and manufacturing industry standards.</p>
    </div>
    <div class="abs band"><span class="pnum pnum--l">02</span></div>
    <div class="photo" style="left:7px;top:114px;width:141px;height:98px" role="img" aria-label="Dispensary reception counter with green accent wall and shelving"></div>
  </section>

  <!-- our story -->
  <section class="page">
    <div class="abs story__band"></div>
    <div class="photo photo--warm" style="left:7px;top:7px;width:141px;height:100px" role="img" aria-label="Hospitality bar interior with pendant lights and timber shelving"></div>
    <h2 class="abs head story__title">Our Story</h2>
    <div class="abs body story__body">
      <p>Harbourline Interiors Group emerged from a crucial need: assisting two pharmacists in designing and building a medical center and pharmacy. These pharmacists, familiar with Daniel Ashworth's background as both an interior designer and commercial builder, sought his expertise. Despite being retired from the building industry, Daniel was approached to review drawings and quotations for the project, revealing significant design flaws and regulatory non-compliance among the quotes that varied by 40%. Daniel agreed to assist, reactivating his licenses with the Victorian Building Authority. He coordinated with various consultants to refine the design, secure necessary permits, including town planning and change of use, and oversee the project through to completion. Collaborating with a skilled team of industry experts and even his son, Sam, a third-year carpenter apprentice at the time, Daniel ensured the project's success. Inspired by this experience, Daniel and his son Sam have united to support others unfamiliar with the complexities of design and construction compliance in interior fitouts.</p>
    </div>
    <span class="pnum pnum--r">03</span>
  </section>

  <!-- daniel -->
  <section class="page">
    <div class="photo photo--person" style="left:6px;top:6px;width:72px;height:68px" role="img" aria-label="Portrait of the founder"></div>
    <div class="abs person__box"><h2 class="head person__name">Daniel<br>Ashworth</h2></div>
    <div class="abs body person__body">
      <p>Daniel Ashworth is an accomplished interior designer and commercial builder. Graduating as an interior designer in 1992, he faced the challenges of a recessionary job market, which led him to work as a sales representative for a commercial lighting manufacturer for two years. Despite the limited opportunities in his field, Daniel's determination and vision drove him to establish his own interior design practice in 1994.</p>
      <p>In 1996, Daniel solidified his professional standing by becoming a registered interior design practitioner with the National Building Commission, demonstrating his commitment to quality and compliance within the industry. His pursuit of excellence continued as he expanded his skill set, becoming a registered commercial builder in 2000, allowing him to seamlessly integrate design and construction services.</p>
      <p>Daniel is the Founder and CEO of Harbourline Interiors Group, a company dedicated to transforming the commercial and retail fitout industry. With a client-centric approach, the goal is to exceed expectations by delivering exceptional results for projects ranging from medicinal cannabis dispensaries to medical centres, pharmacies, commercial, retail, and hospitality interiors. Their holistic methodology, meticulous planning, and proactive problem-solving ensure that every project is completed on time, on budget, and hassle-free.</p>
    </div>
    <div class="photo photo--fade" style="left:0;right:0;top:170px;bottom:0" role="img" aria-label="Faint glass office tower"></div>
    <span class="pnum pnum--l">04</span>
  </section>

  <!-- sam -->
  <section class="page">
    <div class="abs person__edge"></div>
    <div class="photo photo--person" style="left:6px;top:6px;width:71px;height:68px" role="img" aria-label="Portrait of the carpenter in work jacket"></div>
    <div class="abs person__box person__box--dark"><h2 class="head person__name">Sam<br>Ashworth</h2></div>
    <div class="abs body" style="left:6px;top:80px;width:84px;font-size:2.2px">
      <p>Sam is set to complete his Certificate III carpentry apprenticeship by the end of 2024. His journey has seen him work on a variety of residential and commercial projects, where he has developed a broad skill set in carpentry and site management.</p>
      <p>In June 2024, Sam joined Harbourline Interiors Group, adding a valuable trade-based perspective to the design and construction of fitouts. His hands-on experience and comprehensive skills significantly enhance the team's capability to deliver high-quality projects.</p>
      <p>Sam's expertise includes operating elevated work platforms up to 11 meters (boom lift, scissor lift), reading and interpreting plans, specifications, and drawings for carpentry work, and applying Work Health and Safety requirements, policies, and procedures on all job sites. He is adept at identifying construction work hazards and selecting appropriate risk control strategies. Additionally, Sam can set out design layouts for site construction, is licensed to erect and dismantle restricted height scaffolding, and works safely at heights.</p>
      <p>His ability to conduct workplace communication, provide basic emergency life support (HLTAID002), and administer first aid (HLTAID003) further underscores his comprehensive skill set. Sam's dedication to his craft and his practical expertise make him a key asset to HIG.</p>
    </div>
    <div class="photo photo--site" style="left:94px;top:80px;width:55px;height:64px" role="img" aria-label="Carpenter cutting timber on site"></div>
    <div class="photo photo--warm" style="left:94px;top:147px;width:55px;height:66px" role="img" aria-label="Timber panelled corridor with skylight"></div>
    <span class="pnum pnum--r">05</span>
  </section>

  <!-- teams -->
  <section class="page">
    <div class="abs teams__band"></div>
    <div class="photo" style="left:0;top:7px;width:44px;height:108px;opacity:.35" role="img" aria-label="Faded engineer in hard hat"></div>
    <div class="photo" style="left:44px;top:7px;width:104px;height:105px" role="img" aria-label="Two engineers in hard hats reviewing plans"></div>
    <h2 class="abs head teams__title">Our Expert Teams:</h2>
    <div class="abs team" style="top:128px">
      <div class="team__head"><span class="icon-box"><i></i></span><span>Consulting<br>Team:</span></div>
      <p class="body">Our consulting team comprises project managers, interior designers, architects, town planners, acoustic, structural, mechanical, fire services engineers, building surveyors, and DDA consultants, ensuring compliant and innovative design and construction solutions.</p>
    </div>
    <div class="abs team" style="top:153px">
      <div class="team__head"><span class="icon-box"><i></i></span><span>Construction<br>Team:</span></div>
      <p class="body">The HIG construction team consists of skilled professionals, including site supervisors, carpenters, plasterers, electricians, data and IT specialists, security experts, plumbers, flooring specialists, joiners, glaziers, and painters.</p>
    </div>
    <div class="abs team" style="top:177px">
      <div class="team__head"><span class="icon-box"><i></i></span><span>Finance<br>Team:</span></div>
      <p class="body">Explore fitout and construction finance options with our finance consulting team, providing you with alternatives to fund your projects without tapping into your business, home loan, or superannuation.</p>
    </div>
    <span class="pnum pnum--l">06</span>
  </section>

  <!-- services -->
  <section class="page">
    <h2 class="abs head services__title" style="text-transform:none">Services We Offer:</h2>
    <p class="abs services__sub">Lead project consultant, project management, and construction management</p>
    <div class="abs svc" style="left:6px;top:18px"><span class="icon-box"><i></i></span><span><b>Site inspection:</b>Pre-lease site inspections and advice on base building works.</span></div>
    <div class="abs svc" style="left:77px;top:18px"><span class="icon-box"><i></i></span><span><b>Town planning:</b>Assessment for occupancy use and change of use.</span></div>
    <div class="abs svc" style="left:6px;top:36px"><span class="icon-box"><i></i></span><span><b>Budgeting:</b>Expert advice on construction budgets and required services.</span></div>
    <div class="abs svc" style="left:77px;top:36px"><span class="icon-box"><i></i></span><span><b>Planning services:</b>Comprehensive planning from start to finish.</span></div>
    <div class="abs svc" style="left:6px;top:54px"><span class="icon-box"><i></i></span><span><b>Permit applications:</b>Assistance in obtaining building, health, and town planning permits.</span></div>
    <div class="abs svc" style="left:77px;top:54px"><span class="icon-box"><i></i></span><span><b>Design approval:</b>Submission and approval processes for design fitouts in shopping centers and commercial body corporations.</span></div>
    <div class="abs svc" style="left:6px;top:72px"><span class="icon-box"><i></i></span><span><b>Joinery manufacturing</b>Specialized joinery solutions for all needs.</span></div>
    <div class="abs svc" style="left:77px;top:72px"><span class="icon-box"><i></i></span><span><b>Design and construction</b>Seamless coordination of design and construction solutions.</span></div>
    <div class="abs svc" style="left:6px;top:89px"><span class="icon-box"><i></i></span><span><b>Consultation:</b>Collaborate with disability access consultants, architects, interior designers, and various engineering disciplines.</span></div>
    <div class="abs svc" style="left:77px;top:89px"><span class="icon-box"><i></i></span><span><b>Renovations and rebranding:</b>Vacant and demolishing works, shop front renovations, signage updates, and removals.</span></div>
    <div class="abs services__band"><span class="pnum pnum--r" style="color:#fff;border-color:#fff">07</span></div>
    <div class="photo photo--keys" style="left:0;top:113px;width:125px;height:100px" role="img" aria-label="Keyboard with a gold key and red service key"></div>
  </section>

  <!-- process -->
  <section class="page">
    <p class="abs process__intro">Designing and constructing compliant commercial interiors involves a systematic approach that ensures adherence to regulations and standards set by authorities such as the Victorian Building Authority (VBA). This process methodology outlines key steps to achieve a successful project outcome while meeting legal requirements.</p>

    <div class="step" style="top:28px">
      <p class="step__desc" style="left:14px;text-align:right">The process begins with an initial consultation where client requirements, objectives and constraints are discussed to set clear goals.</p>
      <svg style="left:72px" viewBox="0 0 22 25"><polygon points="11,0 22,6.25 22,18.75 11,25 0,18.75 0,6.25" fill="#1c58b3"/><polygon points="11,2.5 19.8,7.5 19.8,17.5 11,22.5 2.2,17.5 2.2,7.5" fill="#fff"/><polygon points="11,4 18.4,8.3 18.4,16.7 11,21 3.6,16.7 3.6,8.3" fill="#1c58b3"/><text x="11" y="16.8" text-anchor="middle" font-family="Montserrat,sans-serif" font-size="12" fill="#fff">1</text></svg>
      <span class="step__title" style="left:97px">Initial Consultation<br>and Briefing</span>
    </div>
    <div class="step" style="top:54px">
      <span class="step__title" style="right:103px;text-align:right">Concept<br>Development<br>and Design</span>
      <svg style="left:52px" viewBox="0 0 22 25"><polygon points="11,0 22,6.25 22,18.75 11,25 0,18.75 0,6.25" fill="#5b97d6"/><polygon points="11,2.5 19.8,7.5 19.8,17.5 11,22.5 2.2,17.5 2.2,7.5" fill="#fff"/><polygon points="11,4 18.4,8.3 18.4,16.7 11,21 3.6,16.7 3.6,8.3" fill="#5b97d6"/><text x="11" y="16.8" text-anchor="middle" font-family="Montserrat,sans-serif" font-size="12" fill="#fff">2</text></svg>
      <p class="step__desc" style="left:78px">Following the briefing, designers and architects develop concept layouts and plans aligned with the client vision and codes.</p>
    </div>
    <div class="step" style="top:80px">
      <p class="step__desc" style="left:14px;text-align:right">Once the concept is approved, detailed drawings, specifications and documentation are prepared to support building approvals.</p>
      <svg style="left:72px" viewBox="0 0 22 25"><polygon points="11,0 22,6.25 22,18.75 11,25 0,18.75 0,6.25" fill="#1c58b3"/><polygon points="11,2.5 19.8,7.5 19.8,17.5 11,22.5 2.2,17.5 2.2,7.5" fill="#fff"/><polygon points="11,4 18.4,8.3 18.4,16.7 11,21 3.6,16.7 3.6,8.3" fill="#1c58b3"/><text x="11" y="16.8" text-anchor="middle" font-family="Montserrat,sans-serif" font-size="12" fill="#fff">3</text></svg>
      <span class="step__title" style="left:97px">Detailed<br>Design and<br>Documentation</span>
    </div>
    <div class="step" style="top:106px">
      <span class="step__title" style="right:103px;text-align:right">Regulatory<br>Compliance<br>Review</span>
      <svg style="left:52px" viewBox="0 0 22 25"><polygon points="11,0 22,6.25 22,18.75 11,25 0,18.75 0,6.25" fill="#5b97d6"/><polygon points="11,2.5 19.8,7.5 19.8,17.5 11,22.5 2.2,17.5 2.2,7.5" fill="#fff"/><polygon points="11,4 18.4,8.3 18.4,16.7 11,21 3.6,16.7 3.6,8.3" fill="#5b97d6"/><text x="11" y="16.8" text-anchor="middle" font-family="Montserrat,sans-serif" font-size="12" fill="#fff">4</text></svg>
      <p class="step__desc" style="left:78px">Prior to submission, all documentation is reviewed for VBA compliance, fire safety, access and structural requirements.</p>
    </div>
    <div class="step" style="top:132px">
      <p class="step__desc" style="left:14px;text-align:right">With compliant documentation in hand, permits and approvals are secured from the building surveyor and relevant authorities.</p>
      <svg style="left:72px" viewBox="0 0 22 25"><polygon points="11,0 22,6.25 22,18.75 11,25 0,18.75 0,6.25" fill="#1c58b3"/><polygon points="11,2.5 19.8,7.5 19.8,17.5 11,22.5 2.2,17.5 2.2,7.5" fill="#fff"/><polygon points="11,4 18.4,8.3 18.4,16.7 11,21 3.6,16.7 3.6,8.3" fill="#1c58b3"/><text x="11" y="16.8" text-anchor="middle" font-family="Montserrat,sans-serif" font-size="12" fill="#fff">5</text></svg>
      <span class="step__title" style="left:97px">Permitting and<br>Approvals</span>
    </div>
    <div class="step" style="top:158px">
      <span class="step__title" style="right:103px;text-align:right">Construction<br>and Project<br>Management</span>
      <svg style="left:52px" viewBox="0 0 22 25"><polygon points="11,0 22,6.25 22,18.75 11,25 0,18.75 0,6.25" fill="#5b97d6"/><polygon points="11,2.5 19.8,7.5 19.8,17.5 11,22.5 2.2,17.5 2.2,7.5" fill="#fff"/><polygon points="11,4 18.4,8.3 18.4,16.7 11,21 3.6,16.7 3.6,8.3" fill="#5b97d6"/><text x="11" y="16.8" text-anchor="middle" font-family="Montserrat,sans-serif" font-size="12" fill="#fff">6</text></svg>
      <p class="step__desc" style="left:78px">Once permits are obtained, construction begins under close supervision, coordinating trades and site inspections daily.</p>
    </div>
    <div class="step" style="top:184px">
      <p class="step__desc" style="left:14px;text-align:right">Final inspections confirm the works meet approved plans before the completed fitout is handed over to the client.</p>
      <svg style="left:72px" viewBox="0 0 22 25"><polygon points="11,0 22,6.25 22,18.75 11,25 0,18.75 0,6.25" fill="#1c58b3"/><polygon points="11,2.5 19.8,7.5 19.8,17.5 11,22.5 2.2,17.5 2.2,7.5" fill="#fff"/><polygon points="11,4 18.4,8.3 18.4,16.7 11,21 3.6,16.7 3.6,8.3" fill="#1c58b3"/><text x="11" y="16.8" text-anchor="middle" font-family="Montserrat,sans-serif" font-size="12" fill="#fff">7</text></svg>
      <span class="step__title" style="left:97px">Final Inspections<br>and Handover</span>
    </div>
    <span class="pnum pnum--l">08</span>
  </section>

  <!-- case study -->
  <section class="page">
    <div class="abs" style="left:0;right:0;top:0;height:107px;background:var(--blue-deep)"></div>
    <div class="photo" style="left:6px;top:7px;width:143px;height:98px" role="img" aria-label="Dispensary reception counter with green accent wall"></div>
    <p class="abs case__label">Casey study</p>
    <h2 class="abs case__title">Verdant Health dispensary medical centre</h2>
    <p class="abs case__meta"><b>Location:</b> <span class="blue-txt">Ashvale, Victoria</span><br><b>Services:</b> <span class="blue-txt">Design and construct</span></p>
    <div class="abs case__list">
      <p style="font-size:2.5px;font-weight:600;color:var(--ink);margin-bottom:2px">Complaint with:</p>
      <ul class="bullets">
        <li>National Construction Code (NCC) 2022</li>
        <li>Disability Discrimination Act 1992 (DDA)</li>
        <li>Pharmacy Board of Australia (Ahpra)</li>
        <li>Office of Drug Control (ODC)<br>Australian Government</li>
        <li>Therapeutic Goods Administration (TGA)</li>
      </ul>
    </div>
    <div class="photo" style="left:78px;top:117px;width:71px;height:45px" role="img" aria-label="Clinic waiting area with green chairs"></div>
    <div class="photo" style="left:78px;top:166px;width:71px;height:46px" role="img" aria-label="Consulting corridor with wall graphic and seating"></div>
    <span class="pnum pnum--r">09</span>
  </section>

  <!-- vault build -->
  <section class="page build">
    <div class="abs caption" style="left:4px;top:33px;width:72px"><span>Construction of a new 10.5 tone vault to dispense Medicinal Cannabis in accordance with the Office of Drug Control (ODC) and the Pharmacy Boardof Australia.</span></div>
    <div class="photo photo--site" style="left:78px;top:0;width:77px;height:100px" role="img" aria-label="Vault floor slab under construction in empty tenancy"></div>
    <div class="photo photo--dark" style="left:0;top:100px;width:78px;height:63px" role="img" aria-label="Steel vault walls being installed"></div>
    <div class="photo photo--dark" style="left:78px;top:100px;width:77px;height:63px" role="img" aria-label="Vault door installed"></div>
    <div class="photo photo--site" style="left:0;top:163px;width:78px;height:56px" role="img" aria-label="Vault room in finished tenancy"></div>
    <div class="photo" style="left:78px;top:163px;width:77px;height:56px" role="img" aria-label="Vault entry with protected floor"></div>
    <span class="pnum pnum--l" style="background:#fff">10</span>
  </section>

  <!-- walls build -->
  <section class="page build">
    <div class="photo photo--site" style="left:0;top:0;width:78px;height:100px" role="img" aria-label="Stripped tenancy with scissor lift"></div>
    <div class="abs caption" style="left:81px;top:30px;width:70px"><span>Construction of acoustically rated solid plaster walls, new airconditioning system and installation of joinery in accordance with the Pharmacy Board</span></div>
    <div class="photo photo--site" style="left:0;top:100px;width:52px;height:63px" role="img" aria-label="Wall framing in progress"></div>
    <div class="photo photo--site" style="left:52px;top:100px;width:51px;height:63px" role="img" aria-label="Plasterboard walls under construction"></div>
    <div class="photo" style="left:103px;top:100px;width:52px;height:63px" role="img" aria-label="Ceiling and services installation"></div>
    <div class="photo" style="left:0;top:163px;width:78px;height:56px" role="img" aria-label="Completed dispensary with white joinery"></div>
    <div class="photo" style="left:78px;top:163px;width:77px;height:56px" role="img" aria-label="Completed counter and shelving"></div>
    <span class="pnum pnum--r" style="background:#fff">11</span>
  </section>

</main>
</body>
</html>
```